M25 Billboard Advert Required Please

I need an advert for a motorway Billboard on the M25 , the advert should show the following in big letters:
GUTTER CLEANING
DALRYNFLUES.COM and a small logo off to the side (Our logo is attached)

The printer has requested the following (Important please) the advert has to be
pdf file / 300 dpi/landscape orientation / scaled to a minimum 25% advert size ( this particular site is 22ft x 10ft so 25% of this please). Please also make sure that the artwork is embedded and outlined correctly if this is incorrect it will affect the printing of the banner.

Target Market(s)

General Public

Industry/Entity Type

Gutter Cleaning

Requirements
Should not have
• No Change to our Logo

```html
<!DOCTYPE html>
<html lang="en">
<head>
<meta charset="utf-8">
<title>Dalryn Flues – Gutter Cleaning Billboard</title>
<link rel="stylesheet" href="https://fonts.googleapis.com/css2?family=Montserrat:wght@400;600;700&family=Open+Sans:wght@600&display=swap">
<style>
  :root {
    --backdrop: #231f20;
    --brand-red: #e8001c;
    --ink: #111111;
    --band: #000000;
    --paper-light: #ffffff;
    --paper-edge: #c9c9c9;
    --url-white: #ffffff;
  }
  html, body {
    margin: 0;
    padding: 0;
    width: 1200px;
    height: 1200px;
    overflow: hidden;
    background: var(--backdrop);
  }
  .canvas {
    position: relative;
    width: 1200px;
    height: 1200px;
  }
  .billboard {
    position: absolute;
    left: 50px;
    top: 350px;
    width: 1100px;
    height: 499px;
    display: block;
  }
  .brand-name {
    font-family: "Montserrat", sans-serif;
    font-weight: 700;
    font-size: 38px;
    fill: var(--ink);
  }
  .brand-mark { fill: var(--ink); }
  .tagline {
    font-family: "Open Sans", sans-serif;
    font-weight: 600;
    font-size: 19px;
    fill: #222222;
  }
  .headline {
    font-family: "Montserrat", sans-serif;
    font-weight: 700;
    fill: var(--brand-red);
  }
  .headline--main { font-size: 214px; }
  .headline--sub { font-size: 110px; }
  .web-address {
    font-family: "Montserrat", sans-serif;
    font-size: 54px;
    font-weight: 400;
    fill: var(--url-white);
  }
  .web-address__domain {
    font-weight: 700;
    fill: var(--brand-red);
  }
</style>
</head>
<body>
<main class="canvas">
  <svg class="billboard" viewBox="0 0 1100 499" xmlns="http://www.w3.org/2000/svg" aria-label="Gutter cleaning billboard for Dalryn Flues">
    <defs>
      <radialGradient id="paper" cx="50%" cy="55%" r="65%">
        <stop offset="0" stop-color="var(--paper-light)"/>
        <stop offset="1" stop-color="var(--paper-edge)"/>
      </radialGradient>
      <linearGradient id="strip" x1="0" x2="1" y1="0" y2="0">
        <stop offset="0" stop-color="#bdbdbd"/>
        <stop offset="0.5" stop-color="#f4f4f4"/>
        <stop offset="1" stop-color="#bdbdbd"/>
      </linearGradient>
    </defs>

    <rect class="billboard__paper" x="0" y="0" width="1100" height="499" fill="url(#paper)"/>

    <g class="brand">
      <rect class="brand-mark" x="398" y="32" width="34" height="34"/>
      <text class="brand-name" x="446" y="64">Dalryn Flues</text>
      <text class="tagline" x="550" y="107" text-anchor="middle">Clean gutters protect your property</text>
    </g>

    <text class="headline headline--main" x="146" y="297" textLength="807" lengthAdjust="spacingAndGlyphs">GUTTER</text>
    <text class="headline headline--sub" x="146" y="387" textLength="807" lengthAdjust="spacing">CLEANING</text>

    <rect class="billboard__band" x="0" y="411" width="1100" height="68" fill="var(--band)"/>
    <text class="web-address" x="156" y="465" textLength="788" lengthAdjust="spacing">WWW.<tspan class="web-address__domain">DALRYNFLUES</tspan>.COM</text>

    <rect class="billboard__strip" x="0" y="479" width="1100" height="20" fill="url(#strip)"/>
  </svg>
</main>
</body>
</html>
```